label design for oral care product

Kindly invite you to design bottle label (114 mm*40 mm) for our product, a kind of oral care product. The GEL is different from our previous cleanser product, as the pic we uploaded for demonstration. The color of frosted glass bottle is dark green, but the cap is white. You could download the pic of bottle among the uploaded files. The logo file and label content description are attached too. Please check them. Our product is made from many kinds of natural plant extracts, which includes herb and fruit. I wish the label would make our product look high-end and reliable. And it would be better if you could give some advice on paper material and special requirements for printing, related to your design. I value the texture of label too, because I think that stands for the quality of products. No color limitation for the use of our logo.
Target Market(s)
20-40 female, who value oral health.
Colors
Designer to choose colors to be used in the design.
Look and feel
Each slider illustrates characteristics of the customer's brand and the style your logo design should communicate.

```html
<!DOCTYPE html>
<html lang="en">
<head>
<meta charset="utf-8">
<title>Aligner Gel – Bottle Label Dieline</title>
<link rel="stylesheet" href="https://fonts.googleapis.com/css2?family=Architects+Daughter&family=Nunito+Sans:wght@300;400&family=Quicksand:wght@600;700&display=swap">
<style>
  :root {
    --paper: #ffffff;
    --bleed-grey: #5f5f5f;
    --die-red: #e3151f;
    --coral: #ef6a58;
    --olive: #aaa83e;
    --ink: #1d1d1b;
    --sketch: #2b2b2b;
    --leaf-green: #8cc43f;
    --logo-green: #3fb56a;
    --sun-yellow: #fff01f;
    --guide-green: #2fd12f;
  }
  html, body { margin: 0; padding: 0; overflow: hidden; background: var(--paper); }
  .canvas { position: relative; width: 1200px; height: 1200px; overflow: hidden; background: var(--paper); }
  .abs { position: absolute; }

  .bleed-area { left: 21px; top: 215px; width: 1162px; height: 773px; background: var(--bleed-grey); }
  .bleed-line { left: 61px; top: 258px; width: 1095px; height: 702px; border: 1px solid var(--die-red); box-sizing: border-box; }

  .label { left: 104px; top: 300px; width: 1010px; height: 618px; background: var(--paper); border-top: 2px solid #111; box-sizing: border-box; }
  .glue-area { left: 104px; top: 300px; width: 65px; height: 618px; background: var(--coral); }
  .front-panel { left: 383px; top: 300px; width: 521px; height: 618px; background: var(--coral); }
  .side-panel { background: var(--olive); border-radius: 6px; }
  .side-left { left: 188px; top: 319px; width: 178px; height: 588px; }
  .side-right { left: 918px; top: 319px; width: 178px; height: 588px; }

  .directions {
    left: 196px; top: 399px; height: 400px; width: 164px;
    writing-mode: vertical-rl; font-family: "Nunito Sans", sans-serif; color: var(--ink);
    display: flex; flex-direction: column; justify-content: center; align-items: center;
  }
  .directions h2 { margin: 0 0 4px 0; font-weight: 400; font-size: 35px; line-height: 38px; }
  .directions p { margin: 0; font-weight: 300; font-size: 18.5px; line-height: 28px; text-align: center; white-space: nowrap; }
  .made-in { left: 188px; top: 828px; width: 178px; text-align: center; font-family: "Nunito Sans", sans-serif; font-size: 20px; letter-spacing: -0.5px; color: var(--ink); }

  .contains {
    left: 926px; top: 408px; height: 390px; width: 134px;
    writing-mode: vertical-rl; transform: rotate(180deg);
    font-family: "Nunito Sans", sans-serif; color: var(--ink);
    display: flex; flex-direction: column; justify-content: center; align-items: center;
  }
  .contains h2 { margin: 0 0 2px 0; font-weight: 400; font-size: 35px; line-height: 38px; }
  .contains p { margin: 0; font-weight: 300; font-size: 18px; line-height: 22px; text-align: center; white-space: nowrap; }

  .brand-name {
    left: 520px; top: 338px; width: 240px; text-align: center;
    font-family: "Quicksand", sans-serif; font-weight: 700; font-size: 52px; line-height: 48px; color: var(--logo-green);
  }
  .brand-dot { left: 740px; top: 340px; width: 16px; height: 16px; border-radius: 50%; background: var(--logo-green); }

  .art { border-radius: 50% 8% 50% 8%; }
  .art-leaf-top { left: 345px; top: 322px; width: 105px; height: 150px; background: #c8d94a; transform: rotate(-20deg); }
  .art-fruit-top { left: 777px; top: 322px; width: 78px; height: 62px; background: #f6b53e; border-radius: 50%; }
  .art-berries { left: 828px; top: 426px; width: 104px; height: 126px; background: #ea6c30; border-radius: 45%; }
  .art-paisley { left: 420px; top: 512px; width: 92px; height: 102px; background: #f7c97a; }
  .art-small-leaf { left: 760px; top: 577px; width: 45px; height: 72px; background: #93c45a; }
  .art-fern-leaf { left: 416px; top: 652px; width: 112px; height: 138px; background: #d8df8c; }
  .art-big-leaf { left: 800px; top: 634px; width: 140px; height: 150px; background: #e0a263; }
  .art-tooth { left: 524px; top: 496px; width: 248px; height: 186px; background: rgba(140,196,63,0.35); border-radius: 42% 42% 46% 46%; }

  .product-name {
    left: 526px; top: 528px; width: 244px; text-align: center; color: var(--paper);
    font-family: "Quicksand", sans-serif; font-weight: 700;
  }
  .product-name .line-1 { display: block; font-size: 48px; line-height: 52px; letter-spacing: 1px; }
  .product-name .line-2 { display: block; font-size: 60px; line-height: 58px; letter-spacing: 2px; }

  .claim {
    left: 500px; top: 696px; width: 290px; text-align: center; color: var(--sun-yellow);
    font-family: "Quicksand", sans-serif; font-weight: 700; font-size: 26px; line-height: 26px; letter-spacing: 1px;
  }

  .banner { left: 470px; top: 790px; width: 376px; height: 72px; }
  .banner-text {
    left: 470px; top: 801px; width: 376px; text-align: center; color: var(--paper);
    font-family: "Quicksand", sans-serif; font-weight: 700; font-size: 18.5px; line-height: 25px; white-space: nowrap;
  }
  .volume {
    left: 590px; top: 876px; width: 137px; text-align: center; color: var(--paper);
    font-family: "Nunito Sans", sans-serif; font-size: 15px;
  }

  .dim-tag {
    font-family: "Nunito Sans", sans-serif; font-weight: 400; font-size: 16px; color: var(--die-red);
    background: var(--paper); border: 1px solid var(--die-red); padding: 0 4px; line-height: 22px;
  }
  .note { font-family: "Architects Daughter", cursive; color: var(--sketch); font-size: 24px; letter-spacing: 1px; }
  .overlay { left: 0; top: 0; width: 1200px; height: 1200px; pointer-events: none; }
</style>
</head>
<body>
<main class="canvas">
  <div class="abs bleed-area"></div>
  <div class="abs bleed-line"></div>

  <section class="abs label"></section>
  <div class="abs glue-area"></div>
  <div class="abs front-panel"></div>
  <div class="abs side-panel side-left"></div>
  <div class="abs side-panel side-right"></div>

  <div class="abs directions">
    <h2>Directions:</h2>
    <p>Drop on the teeth directly after<br>brushing. Or, put into clear aligners before<br>wearing again. No need to rinse your<br>mouth with water.</p>
  </div>
  <div class="abs made-in">Made in Taiwan</div>

  <div class="abs contains">
    <h2>Contains:</h2>
    <p>A proprietary blend of natural<br>plant extract including Angelica, Radix<br>Rehmanniae, Coptis, Honeysuckle, Echina<br>cea, Sage, Chamomile, Acerola cherry.</p>
  </div>

  <div class="abs art art-leaf-top" role="img" aria-label="Illustrated light green leaf"></div>
  <div class="abs art-fruit-top" role="img" aria-label="Illustrated yellow fruit sprig"></div>
  <div class="abs art-berries" role="img" aria-label="Illustrated orange berry branch"></div>
  <div class="abs art art-paisley" role="img" aria-label="Illustrated decorative peach leaf"></div>
  <div class="abs art art-small-leaf" role="img" aria-label="Illustrated small green fern leaf"></div>
  <div class="abs art art-fern-leaf" role="img" aria-label="Illustrated pale green fern leaf"></div>
  <div class="abs art art-big-leaf" role="img" aria-label="Illustrated tan leaf"></div>
  <div class="abs art-tooth" role="img" aria-label="Green tooth outline illustration framing the product name"></div>

  <div class="abs brand-name">brisa<br>mint</div>
  <div class="abs brand-dot"></div>

  <div class="abs product-name"><span class="line-1">ALIGNER</span><span class="line-2">GEL</span></div>

  <div class="abs claim">IMMUNE<br>SUPPORT FOR<br>ORAL HEALTH</div>

  <svg class="abs banner" viewBox="0 0 376 72" aria-hidden="true">
    <path d="M2 24 H60 V10 Q188 -6 316 10 V24 H374 V70 H2 Z" fill="none" stroke="var(--paper)" stroke-width="2"/>
    <path d="M7 29 H65 V15 Q188 0 311 15 V29 H369 V65 H7 Z" fill="none" stroke="var(--paper)" stroke-width="2"/>
  </svg>
  <div class="abs banner-text">The Solution to Maintain<br>Dental Hygiene and Strengthen Gums</div>

  <svg class="abs overlay" viewBox="0 0 1200 1200" aria-hidden="true">
    <ellipse cx="524" cy="886" rx="66" ry="2.5" fill="var(--sun-yellow)"/>
    <ellipse cx="792" cy="886" rx="66" ry="2.5" fill="var(--sun-yellow)"/>
  </svg>
  <div class="abs volume">30 ml / 1 fl oz</div>

  <svg class="abs overlay" viewBox="0 0 1200 1200" aria-hidden="true">
    <g stroke="var(--guide-green)" stroke-width="1">
      <line x1="609" y1="300" x2="609" y2="918"/>
      <line x1="104" y1="607" x2="1114" y2="607"/>
    </g>
    <g fill="none" stroke="var(--die-red)" stroke-width="3">
      <circle cx="104" cy="300" r="11"/>
      <circle cx="1114" cy="300" r="11"/>
      <circle cx="104" cy="918" r="11"/>
      <circle cx="383" cy="918" r="11"/>
      <circle cx="904" cy="918" r="11"/>
    </g>
    <g stroke="var(--sketch)" stroke-width="1.5" fill="none">
      <line x1="85" y1="203" x2="1122" y2="203"/>
      <line x1="106" y1="162" x2="106" y2="1095"/>
      <line x1="1114" y1="127" x2="1114" y2="1090"/>
      <line x1="169" y1="960" x2="169" y2="1135"/>
      <line x1="383" y1="960" x2="383" y2="1090"/>
      <line x1="900" y1="960" x2="900" y2="1090"/>
      <line x1="25" y1="1024" x2="1150" y2="1024"/>
      <line x1="8" y1="302" x2="118" y2="302"/>
      <line x1="6" y1="918" x2="118" y2="918"/>
      <line x1="41" y1="270" x2="41" y2="960"/>
      <path d="M68 255 C55 200 80 140 120 116"/>
      <line x1="98" y1="1034" x2="112" y2="1012"/>
      <line x1="162" y1="1034" x2="176" y2="1012"/>
      <line x1="376" y1="1034" x2="390" y2="1012"/>
      <line x1="888" y1="1040" x2="902" y2="1010"/>
      <line x1="1090" y1="1048" x2="1116" y2="1012"/>
      <line x1="32" y1="310" x2="48" y2="288"/>
      <line x1="32" y1="928" x2="50" y2="900"/>
    </g>
  </svg>

  <div class="abs dim-tag" style="left:583px; top:263px;">7 cm</div>
  <div class="abs dim-tag" style="left:114px; top:599px;">4 cm</div>
  <div class="abs dim-tag" style="left:617px; top:881px;">4 cm</div>

  <div class="abs note" style="left:790px; top:26px; font-size:30px;">(DIE LINE/ARTWORK)</div>
  <div class="abs note" style="left:124px; top:100px;">&#9656; BLEED AREA</div>
  <div class="abs note" style="left:501px; top:162px; font-size:27px;">FULL LABLE LEN</div>
  <div class="abs note" style="left:22px; top:625px; font-size:24px; transform:rotate(-90deg); transform-origin:left top;">HEIGHT</div>
  <div class="abs note" style="left:110px; top:1038px; font-size:16px; line-height:20px;">GLU<br>AREA</div>
  <div class="abs note" style="left:201px; top:1036px;">SIDE LABLE</div>
  <div class="abs note" style="left:563px; top:1044px; font-size:26px;">FRONT WIDTH</div>
  <div class="abs note" style="left:942px; top:1040px; line-height:26px;">SIDE<br>&nbsp;LABLE</div>
</main>
</body>
</html>
```